lunch and dinne(al a carte) menus

we are a medium sized licenced club that has taken back the dining in the club
in the western suburbs of sydney working class with a rugby league base
our logo is a wolf kelford hawks

Reason: We have changed the name to Bluegate grill it could be done as Bluegate or Bluegate or Bluegate We need a lunch menu and a seperate dinner menu eg Bluegate grill l u n c h or Bluegate grill d i n n e r

Reason: Weve changed the name

Target Market(s)

young families, working class rugby leagues sporty types

Industry/Entity Type

Club

Requirements
Must have
• user friendly

```html
<!DOCTYPE html>
<html lang="en">
<head>
<meta charset="utf-8">
<title>Bluegate grill – menu cover</title>
<link rel="stylesheet" href="https://fonts.googleapis.com/css2?family=Lora:ital,wght@1,600&display=swap">
<style>
  :root {
    --paper: #ffffff;
    --slate: #687a72;
    --lime: #a4c14f;
    --coral: #ef6b5c;
    --teal: #5fbfa4;
    --olive-dark: #4f4a38;
    --cream: #f6f1dc;
  }
  * { margin: 0; padding: 0; box-sizing: border-box; }
  html, body {
    width: 1200px;
    height: 848px;
    overflow: hidden;
    background: var(--paper);
  }
  .canvas {
    position: relative;
    width: 1200px;
    height: 848px;
    background: var(--paper);
  }
  .menu-spread {
    position: absolute;
    left: 241px;
    top: 134px;
    width: 725px;
    height: 482px;
    display: flex;
    gap: 4px;
  }
  .cover-front {
    position: relative;
    width: 360px;
    height: 100%;
    background: var(--slate);
    overflow: hidden;
  }
  .cover-back {
    width: 361px;
    height: 100%;
    background: var(--slate);
  }
  .stripes {
    position: absolute;
    left: 0;
    top: 0;
    width: 360px;
    height: 357px;
    display: flex;
  }
  .stripe { height: 100%; }
  .stripe--lime { background: var(--lime); }
  .stripe--coral { background: var(--coral); }
  .stripe--teal { background: var(--teal); }
  .stripe--slate { background: var(--slate); }
  .cutlery-mark {
    position: absolute;
    left: 101px;
    top: 237px;
    width: 163px;
    height: 81px;
    border-radius: 14px;
    background: var(--olive-dark);
    border: 3px solid var(--cream);
  }
  .name-band {
    position: absolute;
    left: 0;
    top: 357px;
    width: 360px;
    height: 125px;
    display: flex;
    align-items: center;
    justify-content: center;
  }
  .venue-name {
    font-family: "Lora", Georgia, serif;
    font-style: italic;
    font-weight: 600;
    font-size: 23px;
    color: var(--cream);
    letter-spacing: 0.2px;
    transform: translateY(-8px);
  }
</style>
</head>
<body>
  <main class="canvas">
    <section class="menu-spread">
      <div class="cover-front">
        <div class="stripes">
          <span class="stripe stripe--lime" style="width:41px"></span>
          <span class="stripe stripe--coral" style="width:65px"></span>
          <span class="stripe stripe--slate" style="width:29px"></span>
          <span class="stripe stripe--teal" style="width:69px"></span>
          <span class="stripe stripe--lime" style="width:70px"></span>
          <span class="stripe stripe--slate" style="width:30px"></span>
          <span class="stripe stripe--coral" style="width:56px"></span>
        </div>
        <div class="cutlery-mark" role="img" aria-label="Fork and spoon illustration"></div>
        <div class="name-band">
          <h1 class="venue-name">Bluegate grill</h1>
        </div>
      </div>
      <div class="cover-back"></div>
    </section>
  </main>
</body>
</html>
```